kestrel home systems HERS

Looking for business card design that represents our company. we are kestrel home systems and we dedicate our skills of home energy efficiency to our customer by providing energy solution to their energy problems.
HVAC
SOLAR
INSULLATION
LIGHTING
DUCT TESTING
HERS RATING.

```html
<!DOCTYPE html>
<html lang="en">
<head>
<meta charset="utf-8">
<title>Kestrel Home Systems – Business Card</title>
<link href="https://fonts.googleapis.com/css2?family=Roboto:wght@400;500&family=Roboto+Condensed:wght@400;700&display=swap" rel="stylesheet">
<style>
  :root {
    --backdrop: #e4e4e4;
    --card: #0e0f10;
    --blue: #3db8ea;
    --blue-deep: #1a8fd6;
    --green: #86c42a;
    --white: #ffffff;
    --ink: #1a1a1a;
  }
  * { margin: 0; padding: 0; box-sizing: border-box; }
  html, body { width: 1200px; height: 1033px; overflow: hidden; }
  body {
    background: var(--backdrop);
    font-family: "Roboto", sans-serif;
    color: var(--white);
    position: relative;
  }
  .card {
    position: absolute;
    left: 318px;
    width: 562px;
    height: 340px;
    background: var(--card);
    border-radius: 16px;
    overflow: hidden;
  }
  .card--front { top: 152px; }
  .card--back { top: 540px; }

  .brand {
    position: absolute;
    display: flex;
    align-items: center;
    gap: 12px;
    font-family: "Roboto", sans-serif;
    font-weight: 500;
    color: var(--white);
    white-space: nowrap;
  }
  .brand__dot {
    border-radius: 50%;
    background: var(--blue);
    flex: none;
  }
  .card--front .brand { left: 0; right: 0; justify-content: center; top: 78px; font-size: 36px; }
  .card--front .brand__dot { width: 30px; height: 30px; }
  .card--back .brand { left: 27px; top: 64px; font-size: 32px; }
  .card--back .brand__dot { width: 26px; height: 26px; }

  .services {
    position: absolute;
    left: 0; right: 0;
    top: 205px;
    text-align: center;
    font-size: 14.5px;
    line-height: 21px;
    letter-spacing: 0.2px;
  }
  .services__item { margin: 0 6px; }
  .services__item::before {
    content: "»";
    color: var(--green);
    margin-right: 6px;
    font-size: 12px;
  }
  .front-web {
    position: absolute;
    left: 0; right: 0;
    top: 293px;
    text-align: center;
    font-size: 14.5px;
  }
  .front-web .accent-blue { color: var(--blue); }
  .front-web .accent-green { color: var(--green); }
  .front-bar {
    position: absolute;
    left: 0; right: 0; bottom: 0;
    height: 10px;
    display: flex;
  }
  .front-bar__blue { flex: 1; background: var(--blue); }
  .front-bar__green { flex: 1; background: var(--green); }

  .person { position: absolute; left: 27px; top: 205px; }
  .person__name {
    font-family: "Roboto Condensed", sans-serif;
    font-weight: 700;
    font-size: 23px;
    color: var(--green);
    line-height: 28px;
  }
  .person__role {
    font-family: "Roboto Condensed", sans-serif;
    font-size: 14.5px;
    margin-top: 3px;
  }
  .person__creds {
    font-size: 14.5px;
    line-height: 22px;
    margin-top: 11px;
  }

  .contact {
    position: absolute;
    left: 292px;
    top: 208px;
    list-style: none;
    font-size: 14.5px;
  }
  .contact__row {
    display: flex;
    align-items: center;
    height: 21.5px;
  }
  .contact__icon { width: 14px; height: 14px; margin-right: 14px; flex: none; }

  .license-band {
    position: absolute;
    left: 230px; right: 0; bottom: 0;
    height: 42px;
    background: var(--green);
    clip-path: polygon(16px 0, 100% 0, 100% 100%, 0 100%);
    border-top-left-radius: 10px;
  }
  .license-band__text {
    position: absolute;
    left: 60px; top: 11px;
    font-size: 14.5px;
    color: var(--ink);
  }
  .accent-strip {
    position: absolute;
    left: 0; bottom: 0;
    width: 232px;
    height: 14px;
    background: linear-gradient(90deg, var(--blue-deep) 0%, var(--blue) 45%, #cdeefc 100%);
    clip-path: polygon(0 0, 100% 0, 96% 100%, 0 100%);
  }
</style>
</head>
<body>

<section class="card card--front">
  <div class="brand"><span class="brand__dot"></span>kestrel home systems</div>
  <div class="services">
    <div><span class="services__item">HVAC</span><span class="services__item">SOLAR</span><span class="services__item">INSULLATION</span><span class="services__item">LIGHTING</span></div>
    <div><span class="services__item">DUCT TESTING</span><span class="services__item">HERS RATING</span></div>
  </div>
  <div class="front-web">www.<span class="accent-blue">kestrel</span><span class="accent-green">home</span>systems.net</div>
  <div class="front-bar"><span class="front-bar__blue"></span><span class="front-bar__green"></span></div>
</section>

<section class="card card--back">
  <div class="brand"><span class="brand__dot"></span>kestrel home systems</div>

  <div class="person">
    <div class="person__name">Marisol T. Vega</div>
    <div class="person__role">Energy specialist</div>
    <div class="person__creds">24 Certifications, Duct<br>Testing, H.E.R.S Raters</div>
  </div>

  <ul class="contact">
    <li class="contact__row">
      <svg class="contact__icon" viewBox="0 0 16 16" aria-hidden="true"><path fill="#86c42a" d="M1 5c0-2 3-3 7-3s7 1 7 3v1h-3V4.8C11 4.3 9.5 4 8 4s-3 .3-4 .8V6H1zM4 7h8l2 7H2z"/></svg>
      <span>5550148827</span>
    </li>
    <li class="contact__row">
      <svg class="contact__icon" viewBox="0 0 16 16" aria-hidden="true"><g fill="none" stroke="#86c42a" stroke-width="1.4"><circle cx="8" cy="8" r="6.5"/><ellipse cx="8" cy="8" rx="3" ry="6.5"/><path d="M1.5 8h13M2.5 4.5h11M2.5 11.5h11"/></g></svg>
      <span>www.kestrelhomesystems.net</span>
    </li>
    <li class="contact__row">
      <svg class="contact__icon" viewBox="0 0 16 16" aria-hidden="true"><rect x="1" y="3" width="14" height="10" fill="#86c42a"/><path d="M1 3l7 6 7-6M1 13l5-5M15 13l-5-5" fill="none" stroke="#0e0f10" stroke-width="1.2"/></svg>
      <span>marisol.kestrel@mailbox.com</span>
    </li>
  </ul>

  <div class="accent-strip"></div>
  <div class="license-band"><span class="license-band__text">LIC#402718</span></div>
</section>

</body>
</html>
```